Anzeigengestaltung für Zahnarztpraxis
Zielgruppe
Wir sind eine Zahnarztpraxis in einer ländlichen Gemeinde mit 5000 Einwohnern in der Schweiz und bieten alles, was eine moderne Zahnarztpraxis zu bieten hat: Kieferorthopädie, allgemeine Zahnmedizin, Implantologie (schablonengeführt und digital geplant, Clarodent, Intraoralscanner, 3D-Röntgen
Online-Agenda
Zielgruppe: 4-99
2023: 20 jähriges Jubiläum
Der Text sollte später leicht und von uns selbständig geändert werden können:
z.B.
Frühjahrsputz: 20 Franken Rabatt auf die nächste Prophylaxesitzung
Aktion im April: 20% Rabatt auf Clarodent
Aktion im Mai 20% Rabatt auf Implantatbehandlungen
Sommeraktion Bleaching 495.-
Aufgabenstellung
Maße: 185x63mm, (185x130) beide quer
druckoptimiertes PDF X/-4
Bildauflösung: CMYK- und Graustufenbilder 300dpi
Farbprofil: PSOuncoated v3

```html
<!DOCTYPE html>
<html lang="de">
<head>
<meta charset="utf-8">
<title>Jubiläumsangebot – Praxis Berger Zahnärzte</title>
<link rel="stylesheet" href="https://fonts.googleapis.com/css2?family=Montserrat:wght@300;400;500;700&display=swap">
<style>
  :root {
    --green: #7cbc2a;
    --green-light: #a9d46e;
    --grey-text: #6d6d6d;
    --box-grey: #e4e4e4;
    --paper: #f4f4f4;
    --backdrop: #e9e9ea;
    --white: #ffffff;
  }
  * { box-sizing: border-box; margin: 0; padding: 0; }
  html, body {
    width: 1200px; height: 1200px; overflow: hidden;
    background: var(--backdrop);
    font-family: "Montserrat", sans-serif;
  }
  .ad-card {
    position: absolute; left: 50px; top: 215px;
    width: 1100px; height: 770px;
    background: var(--paper);
    overflow: hidden;
  }
  .hero-photo {
    position: absolute; left: 0; top: 0; width: 1100px; height: 400px;
    background: linear-gradient(100deg, #c7a48c 0%, #b8c4cc 28%, #d3dde4 55%, #a9c6df 80%, #c8d6e2 100%);
  }
  .anniversary-panel {
    position: absolute; left: 60px; top: 360px; width: 280px; height: 410px;
    background: var(--green);
    color: var(--white);
    text-align: center;
    padding-top: 34px;
  }
  .anniversary-kicker { font-size: 24px; font-weight: 400; letter-spacing: 4px; }
  .anniversary-number { font-size: 140px; font-weight: 700; line-height: 1; margin-top: 6px; }
  .anniversary-word { font-size: 52px; font-weight: 300; letter-spacing: 2px; line-height: 1; }
  .offers-title {
    position: absolute; left: 380px; top: 412px;
    font-size: 22px; font-weight: 400; color: var(--green);
    letter-spacing: 22px;
  }
  .offer-grid {
    position: absolute; left: 380px; top: 460px;
    display: grid; grid-template-columns: 320px 320px; gap: 25px 30px;
  }
  .offer {
    height: 110px; background: var(--box-grey);
    display: flex; flex-direction: column; justify-content: center; align-items: center;
    color: var(--grey-text); text-align: center;
  }
  .offer-label { font-size: 15px; font-weight: 400; color: var(--green); }
  .offer-main { font-size: 26px; font-weight: 700; line-height: 1.2; }
  .offer-detail { font-size: 17px; font-weight: 400; }
  .practice-name {
    position: absolute; right: 50px; top: 712px;
    display: flex; align-items: center; gap: 10px;
    font-size: 20px; font-weight: 500; color: var(--green);
  }
  .practice-dot { width: 34px; height: 34px; border-radius: 50%; background: var(--green); }
  .edge-bar {
    position: absolute; right: 0; top: 700px; width: 22px; height: 70px;
    background: var(--green);
  }
</style>
</head>
<body>
  <div class="ad-card">
    <div class="hero-photo" role="img" aria-label="Foto: lächelnde Patientin auf dem Behandlungsstuhl, Zahnarzt mit Spiegel im Vordergrund"></div>

    <div class="anniversary-panel">
      <p class="anniversary-kicker">WIR FEIERN</p>
      <p class="anniversary-number">20</p>
      <p class="anniversary-word">JAHRE</p>
    </div>

    <h2 class="offers-title">JUBILÄUMSANGEBOT</h2>

    <div class="offer-grid">
      <div class="offer">
        <span class="offer-label">Frühjahrsputz</span>
        <span class="offer-main">um nur CHF 20</span>
      </div>
      <div class="offer">
        <span class="offer-label">Aktion im April</span>
        <span class="offer-main">20% Rabatt</span>
        <span class="offer-detail">auf Clarodent</span>
      </div>
      <div class="offer">
        <span class="offer-label">Aktion im Mai</span>
        <span class="offer-main">20% Rabatt</span>
        <span class="offer-detail">auf Implantatbehandlungen</span>
      </div>
      <div class="offer">
        <span class="offer-label">Sommeraktion</span>
        <span class="offer-main">Bleaching</span>
        <span class="offer-detail">um nur CHF 495.-</span>
      </div>
    </div>

    <div class="practice-name">
      <span class="practice-dot"></span>
      <span>Praxis Berger Zahnärzte</span>
    </div>
    <div class="edge-bar"></div>
  </div>
</body>
</html>
```